Corvale Motorized Shade Business Card

Hello, we've had our logo made. Now we are looking for a clean and cool looking business card. One side can just be the logo with any design elements that might look good with it. The other side will be Name, Phone Number and Email. There will not be an address on the card.

```html
<!DOCTYPE html>
<html lang="en">
<head>
<meta charset="utf-8">
<title>Corvale Motorized Shade – Business Card</title>
<link href="https://fonts.googleapis.com/css2?family=Montserrat:wght@500;700&display=swap" rel="stylesheet">
<style>
  :root {
    --bg: #cfe9e4;
    --card: #ffffff;
    --navy: #0d3b7a;
    --sky: #1aa3e0;
    --sun: #fdb913;
  }
  * { box-sizing: border-box; margin: 0; padding: 0; }
  html, body {
    width: 1200px; height: 856px; overflow: hidden;
    background: var(--bg);
    font-family: "Montserrat", sans-serif;
  }
  .stage {
    width: 1200px; height: 856px;
    display: flex; align-items: center; justify-content: center; gap: 60px;
  }
  .card {
    position: relative;
    width: 520px; height: 297px;
    background: var(--card);
    border-radius: 26px;
    box-shadow: 0 6px 18px rgba(20, 70, 80, 0.18);
    overflow: hidden;
  }
  .card-front {
    display: flex; flex-direction: column; align-items: center; justify-content: center;
  }
  .brand-mark {
    display: flex; align-items: center; gap: 14px;
  }
  .brand-dot {
    width: 26px; height: 26px; border-radius: 50%; background: var(--sun);
  }
  .brand-name {
    font-weight: 700; font-size: 58px; letter-spacing: 1px;
    color: var(--navy); text-transform: uppercase; line-height: 1;
  }
  .brand-tagline {
    margin-top: 12px;
    font-weight: 700; font-size: 16px; letter-spacing: 7px;
    color: var(--navy); text-transform: uppercase;
  }
  .card-back .accent-area {
    position: absolute; left: 0; bottom: 0;
    width: 250px; height: 170px;
    background: var(--sun);
  }
  .contact-name {
    position: absolute; left: 230px; top: 46px;
  }
  .contact-name .person {
    font-weight: 700; font-size: 15px; color: var(--navy); text-transform: uppercase;
  }
  .contact-name .role {
    font-weight: 700; font-size: 11px; color: var(--sky); margin-top: 2px;
  }
  .contact-lines {
    position: absolute; right: 34px; top: 172px;
    list-style: none;
  }
  .contact-lines li {
    display: flex; align-items: center; gap: 8px;
    font-weight: 500; font-size: 13px; color: var(--navy);
    margin-bottom: 6px;
  }
  .contact-lines svg { width: 16px; height: 14px; flex: none; }
</style>
</head>
<body>
  <main class="stage">
    <section class="card card-front" aria-label="Card front">
      <div class="brand-mark">
        <span class="brand-dot"></span>
        <span class="brand-name">Corvale</span>
      </div>
      <div class="brand-tagline">Motorized Shade</div>
    </section>

    <section class="card card-back" aria-label="Card back">
      <div class="accent-area" role="img" aria-label="Brand sun decoration area"></div>
      <div class="contact-name">
        <div class="person">Dana Reyes</div>
        <div class="role">Manager</div>
      </div>
      <ul class="contact-lines">
        <li>
          <svg viewBox="0 0 16 14" aria-hidden="true"><rect width="16" height="14" rx="2" fill="var(--sky)"/><path d="M5 3.5c-.6 0-1 .5-1 1 0 3 2.5 5.5 5.5 5.5.5 0 1-.4 1-1l-1.5-1-1 .8c-1-.5-1.8-1.3-2.3-2.3l.8-1z" fill="#fff"/></svg>
          1-800-555-0142
        </li>
        <li>
          <svg viewBox="0 0 16 14" aria-hidden="true"><rect x="1" y="2" width="14" height="10" rx="1" fill="none" stroke="var(--sky)" stroke-width="1.6"/><path d="M1.5 2.8 8 8l6.5-5.2" fill="none" stroke="var(--sky)" stroke-width="1.6"/></svg>
          dana.reyes@corvale.com
        </li>
      </ul>
    </section>
  </main>
</body>
</html>
```